quillmetric corporate presentation

We have a wireframe presentation with 18 slides to be implemented in Google slides (powerpoint optional although we would rather prefer Google slides). Please, be creative and don't take the examples in the wireframe as literal. We also provide the following:

- Color palet
- quillmetric Logos
- Slide wireframe
- slide reference for slide number 5.
- Flyer
- Partner logos

You can find all the materials here: https://files.plinthbox.example/share/7kqTr2mWx9LpBn4Zc

```html
<!DOCTYPE html>
<html lang="en">
<head>
<meta charset="utf-8">
<title>quillmetric corporate presentation</title>
<link href="https://fonts.googleapis.com/css2?family=Poppins:wght@400;500;600;700&display=swap" rel="stylesheet">
<style>
:root{
  --board:#6b6b6b;
  --navy:#0d2b45;
  --ink:#1c2a36;
  --teal:#1a9488;
  --teal-bright:#22a596;
  --night:#07172a;
  --white:#ffffff;
  --mist:#eef1f3;
}
*{box-sizing:border-box;margin:0;padding:0}
html,body{width:1039px;height:1200px;overflow:hidden;background:var(--board);font-family:'Poppins',sans-serif}
.board{position:absolute;left:0;top:0;width:1792px;height:2069px;transform:scale(0.57985);transform-origin:0 0}
.slide{position:absolute;width:767px;height:432px;background:var(--white);overflow:hidden;box-shadow:0 6px 18px rgba(0,0,0,.35);color:var(--ink)}
.col-l{left:118px}.col-r{left:906px}
.row-1{top:141px}.row-2{top:593px}.row-3{top:1045px}.row-4{top:1496px}

.footer{position:absolute;left:0;bottom:0;width:767px;height:32px;background:var(--teal)}
.footer-note{position:absolute;left:0;width:590px;top:10px;text-align:center;color:var(--white);font-size:9px}
.page-no{position:absolute;left:576px;top:6px;width:22px;height:20px;background:var(--white);color:var(--ink);font-size:8px;font-weight:600;text-align:center;line-height:20px}
.footer-brand{position:absolute;right:0;top:-8px;width:150px;height:40px;background:var(--white);display:flex;align-items:center;justify-content:center;gap:5px;font-weight:600;font-size:22px;color:var(--navy)}
.mark{display:inline-block;background:var(--teal)}
.footer-brand .mark{width:10px;height:10px}

.heading{position:absolute;display:flex;align-items:center;gap:11px;font-size:27px;font-weight:700;color:var(--navy)}
.heading .mark{width:12px;height:12px}
.teal-sub{position:absolute;color:var(--teal);font-size:16px;font-weight:600;line-height:25px}
.photo{position:absolute}

/* cover */
.cover{background:radial-gradient(ellipse at 95% 110%,#4a1470 0%,rgba(74,20,112,0) 45%),radial-gradient(ellipse at 15% 115%,#0f4a5c 0%,rgba(15,74,92,0) 50%),var(--night);color:var(--white);text-align:center}
.cover-brand{position:absolute;top:95px;width:100%;font-size:44px;font-weight:600}
.cover-title{position:absolute;top:185px;width:100%;font-size:31px;font-weight:700;line-height:44px}
.cover-title .accent{color:var(--teal-bright)}
.cover-author{position:absolute;top:292px;width:100%;font-size:12.5px;line-height:21px}
.cover-author b{font-weight:600}

/* quote */
.quote{position:absolute;left:67px;top:113px;width:300px;font-size:15.5px;line-height:26.5px;color:var(--ink)}
.quote-by{margin-top:28px}
.photo-circle{left:410px;top:27px;width:326px;height:326px;border-radius:50%;border:5px solid var(--navy);background:radial-gradient(circle at 50% 40%,#d9d4cc,#9c8f80 70%,#6f6356)}

/* about */
.about-photo{left:0;top:0;width:767px;height:300px;background:linear-gradient(180deg,rgba(255,255,255,0) 55%,#fff 100%),linear-gradient(100deg,#6d7c86,#b8bec2 45%,#d7d4cf 70%,#c7c1ba)}
.about-body{position:absolute;left:343px;top:276px;width:360px;font-size:12.5px;line-height:23px;color:var(--ink)}

/* services */
.service{position:absolute;width:260px;height:105px}
.service-icon{position:absolute;left:0;top:0;width:105px;height:105px;border:4px solid var(--navy);border-radius:12px;display:flex;align-items:center;justify-content:center;background:var(--white)}
.service-frame{position:absolute;left:124px;top:8px;width:135px;height:97px;border:1.5px solid var(--navy);border-left:none;border-radius:0 12px 12px 0}
.service-frame::before{content:"";position:absolute;left:-2px;top:-5px;width:8px;height:8px;border-radius:50%;background:var(--navy)}
.service-frame::after{content:"";position:absolute;left:0;bottom:-1.5px;width:60px;border-bottom:2px dotted var(--navy);background:transparent}
.service-dot{position:absolute;left:184px;top:101px;width:9px;height:9px;border-radius:50%;background:var(--navy)}
.service-label{position:absolute;left:130px;top:0;height:105px;display:flex;align-items:center;font-size:15px;font-weight:600;color:var(--navy);line-height:19px}
.service.alt .service-icon{border-color:var(--teal)}
.service.alt .service-frame{border-color:var(--teal)}
.service.alt .service-frame::before,.service.alt .service-dot{background:var(--teal)}
.service.alt .service-frame::after{border-bottom-color:var(--teal)}
.service.alt .service-label{color:var(--teal)}

/* talent */
.lead{position:absolute;left:78px;top:150px;font-size:13.5px;color:var(--ink)}
.perks{position:absolute;left:85px;top:183px;list-style:none;font-size:11px;line-height:22.8px;color:var(--ink)}
.perks li{position:relative;padding-left:21px}
.perks li::before{content:"";position:absolute;left:0;top:8px;width:6px;height:6px;border-radius:50%;background:var(--teal)}
.talent-photo{background:linear-gradient(180deg,#8ea3b3,#2c3f52)}

/* partners */
.halo{position:absolute;background:radial-gradient(circle at 60% 50%,#f2f4f5 0%,rgba(255,255,255,0) 60%);left:0;top:60px;width:767px;height:340px}
.ring{position:absolute;border-radius:50%;background:var(--white)}
.ring-outer{left:259px;top:97px;width:250px;height:250px;border:1px solid #dde1e4;box-shadow:0 4px 18px rgba(0,0,0,.08)}
.ring-mid{left:274px;top:112px;width:220px;height:220px;border:1px solid #d3d8dc}
.ring-core{left:292px;top:130px;width:184px;height:184px;border:1px solid #c9ced3;box-shadow:0 3px 12px rgba(0,0,0,.12);display:flex;align-items:center;justify-content:center;gap:5px;font-weight:600;font-size:21px;color:var(--navy)}
.ring-core .mark{width:10px;height:10px}
.badge{position:absolute;width:126px;height:126px;border-radius:50%;background:var(--white);box-shadow:0 4px 16px rgba(0,0,0,.12);display:flex;align-items:center;justify-content:center}
.badge span{display:block;width:46px;height:46px;border-radius:8px;background:var(--mist)}
.badge span.round{border-radius:50%}

/* engagement */
.work-photo{background:linear-gradient(160deg,#3b5870,#1c2f45)}
.work-label{position:absolute;width:187px;text-align:center;top:330px;font-size:14px;font-weight:700;color:var(--navy)}

/* closing */
.closing{background:linear-gradient(150deg,#17263a 0%,#0c1a2c 45%,#0a1628 100%);color:var(--white);text-align:center}
.closing-brand{position:absolute;top:103px;width:100%;font-size:44px;font-weight:600}
.closing-title{position:absolute;top:180px;width:100%;font-size:58px;font-weight:700}
.closing-title .accent{color:var(--teal)}
.socials{position:absolute;top:278px;left:0;width:100%;display:flex;justify-content:center;gap:15px}
.socials span{width:24px;height:24px;border-radius:4px;background:var(--white)}
</style>
</head>
<body>
<div class="board">

  <!-- Cover -->
  <section class="slide cover col-l row-1">
    <div class="cover-brand">quillmetric</div>
    <h1 class="cover-title"><span class="accent">Leading the Future</span><br>With Data and Intelligence</h1>
    <p class="cover-author"><b>Marta Ribó</b><br>Madrid, 11 Junio 2025</p>
  </section>

  <!-- Talent -->
  <section class="slide col-r row-1">
    <h2 class="heading" style="left:55px;top:36px"><span class="mark"></span>Exceptional talent</h2>
    <p class="teal-sub" style="left:78px;top:85px;width:450px">Work with highly motivated, trained, and committed industry professionals.</p>
    <p class="lead">How do we make it happen</p>
    <ul class="perks">
      <li>Strict selection process</li>
      <li>Competitive pay for premier talent</li>
      <li>Exciting technologies and projects</li>
      <li>100% certification target in 6 months</li>
      <li>10% continuous learning investment (3x market average)</li>
      <li>Culture that draws in the best professionals</li>
    </ul>
    <div class="photo talent-photo" style="left:487px;top:180px;width:78px;height:172px" role="img" aria-label="Photo of a professional seated in a meeting room"></div>
    <div class="photo talent-photo" style="left:575px;top:116px;width:78px;height:236px" role="img" aria-label="Photo of a presenter speaking to colleagues"></div>
    <div class="photo talent-photo" style="left:663px;top:76px;width:78px;height:276px" role="img" aria-label="Photo of a dashboard screen in an office"></div>
    <footer class="footer"><p class="footer-note">© 2025 Companyname.All Rights Reserved &nbsp;|&nbsp; Privacy Policy &nbsp;|&nbsp; Terms of use</p><span class="page-no">05</span><div class="footer-brand"><span class="mark"></span>quillmetric</div></footer>
  </section>

  <!-- Quote -->
  <section class="slide col-l row-2">
    <h2 class="heading" style="left:38px;top:36px"><span class="mark"></span>The future is now</h2>
    <blockquote class="quote">"Generative AI has the potential to add trillions of dollars in value to the global economy and accelerate productivity growth for individuals, businesses, and the economy as a whole."<p class="quote-by">— Halvorsen &amp; Partners</p></blockquote>
    <div class="photo photo-circle" role="img" aria-label="Photo of a team gathered around a table stacking wooden blocks"></div>
    <footer class="footer"><p class="footer-note">© 2025 Companyname.All Rights Reserved &nbsp;|&nbsp; Privacy Policy &nbsp;|&nbsp; Terms of use</p><span class="page-no">02</span><div class="footer-brand"><span class="mark"></span>quillmetric</div></footer>
  </section>

  <!-- Partners -->
  <section class="slide col-r row-2">
    <div class="halo"></div>
    <h2 class="heading" style="left:55px;top:33px"><span class="mark"></span>Outstanding Technologies</h2>
    <div class="ring ring-outer"></div>
    <div class="ring ring-mid"></div>
    <div class="ring ring-core"><span class="mark"></span>quillmetric</div>
    <div class="badge" style="left:103px;top:89px"><span class="round"></span></div>
    <div class="badge" style="left:103px;top:230px"><span></span></div>
    <div class="badge" style="left:540px;top:89px"><span style="background:var(--navy)"></span></div>
    <div class="badge" style="left:540px;top:230px"><span class="round"></span></div>
    <footer class="footer"><p class="footer-note">© 2025 Companyname.All Rights Reserved &nbsp;|&nbsp; Privacy Policy &nbsp;|&nbsp; Terms of use</p><span class="page-no">06</span><div class="footer-brand"><span class="mark"></span>quillmetric</div></footer>
  </section>

  <!-- About -->
  <section class="slide col-l row-3">
    <div class="photo about-photo" role="img" aria-label="Photo of hands over a laptop showing business charts"></div>
    <h2 class="heading" style="left:72px;top:268px"><span class="mark"></span>About Us</h2>
    <p class="teal-sub" style="left:103px;top:312px;width:210px;line-height:21px">Data Analytics &amp; AI for Nonconformists</p>
    <p class="about-body">We are a leading Professional Services company specialized in the design and implementation of cutting edge technologies in Cloud, Data Analytics &amp; AI.</p>
    <footer class="footer"><p class="footer-note">© 2025 Companyname.All Rights Reserved &nbsp;|&nbsp; Privacy Policy &nbsp;|&nbsp; Terms of use</p><span class="page-no">03</span><div class="footer-brand"><span class="mark"></span>quillmetric</div></footer>
  </section>

  <!-- Engagement -->
  <section class="slide col-r row-3">
    <div class="halo"></div>
    <h2 class="heading" style="left:55px;top:33px"><span class="mark"></span>How we work together</h2>
    <div class="photo work-photo" style="left:78px;top:132px;width:187px;height:185px;background:linear-gradient(160deg,#9fb2c4,#c9c0b6)" role="img" aria-label="Photo of an analyst pointing at a dashboard display"></div>
    <div class="photo work-photo" style="left:290px;top:107px;width:187px;height:210px" role="img" aria-label="Photo of two colleagues reviewing a tablet"></div>
    <div class="photo work-photo" style="left:502px;top:75px;width:187px;height:242px;background:linear-gradient(160deg,#5d6f7c,#2a3440)" role="img" aria-label="Photo of a professional working at a laptop"></div>
    <p class="work-label" style="left:78px">Closed Project</p>
    <p class="work-label" style="left:290px">Time &amp; Materials</p>
    <p class="work-label" style="left:502px">Base Line Service</p>
    <footer class="footer"><p class="footer-note">© 2025 Companyname.All Rights Reserved &nbsp;|&nbsp; Privacy Policy &nbsp;|&nbsp; Terms of use</p><span class="page-no">07</span><div class="footer-brand"><span class="mark"></span>quillmetric</div></footer>
  </section>

  <!-- Services -->
  <section class="slide col-l row-4">
    <h2 class="heading" style="left:50px;top:38px"><span class="mark"></span>What we do</h2>
    <div class="service" style="left:97px;top:103px">
      <div class="service-icon"><svg width="36" height="32" viewBox="0 0 36 32" fill="var(--navy)"><rect x="14" y="0" width="8" height="8"/><rect x="2" y="24" width="8" height="8"/><rect x="14" y="24" width="8" height="8"/><rect x="26" y="24" width="8" height="8"/><path d="M17 8h2v7h12v9h-2v-7H19v7h-2v-7H7v7H5v-9h12z"/></svg></div>
      <div class="service-frame"></div><span class="service-dot"></span>
      <p class="service-label">Agentic AI</p>
    </div>
    <div class="service" style="left:410px;top:103px">
      <div class="service-icon"><svg width="40" height="30" viewBox="0 0 40 30" fill="var(--navy)"><circle cx="20" cy="7" r="6"/><circle cx="8" cy="10" r="4.5"/><circle cx="32" cy="10" r="4.5"/><path d="M10 30c0-8 4-13 10-13s10 5 10 13z"/><path d="M0 28c0-6 3-10 8-10 2 0 3 .5 4 1-2 2-3 5-3 9z"/><path d="M40 28c0-6-3-10-8-10-2 0-3 .5-4 1 2 2 3 5 3 9z"/></svg></div>
      <div class="service-frame"></div><span class="service-dot"></span>
      <p class="service-label">AI Agents</p>
    </div>
    <div class="service alt" style="left:97px;top:234px">
      <div class="service-icon"><svg width="34" height="30" viewBox="0 0 34 30" fill="var(--navy)"><path d="M0 0h34v22H0zM3 3v16h28V3z"/><rect x="14" y="22" width="6" height="5"/><rect x="9" y="27" width="16" height="3"/></svg></div>
      <div class="service-frame"></div><span class="service-dot"></span>
      <p class="service-label">Advanced<br>Analytics &amp; ML</p>
    </div>
    <div class="service alt" style="left:410px;top:234px">
      <div class="service-icon"><svg width="40" height="26" viewBox="0 0 40 26" fill="var(--teal)"><path d="M20 0C11 0 4 6 0 13c4 7 11 13 20 13s16-6 20-13C36 6 29 0 20 0zm0 21a8 8 0 1 1 0-16 8 8 0 0 1 0 16z"/><circle cx="20" cy="13" r="4"/></svg></div>
      <div class="service-frame"></div><span class="service-dot"></span>
      <p class="service-label">Data Analytics &amp;<br>Visualization</p>
    </div>
    <footer class="footer"><p class="footer-note">© 2025 Companyname.All Rights Reserved &nbsp;|&nbsp; Privacy Policy &nbsp;|&nbsp; Terms of use</p><span class="page-no">04</span><div class="footer-brand"><span class="mark"></span>quillmetric</div></footer>
  </section>

  <!-- Closing -->
  <section class="slide closing col-r row-4">
    <div class="closing-brand">quillmetric</div>
    <h2 class="closing-title"><span class="accent">Thank</span> You</h2>
    <div class="socials"><span></span><span></span><span></span><span></span></div>
  </section>

</div>
</body>
</html>
```